Birch Hollow Lodge & Harbour. A site that will sell our lifestyle and embody our vision.

We are after a fun interactive website for our property development.
Check out our ideas for layout and content.
Use stock videos and phots if we havent provide enough.
Ive attached our Logo.
We are easy to reach and work with. Love the crative process.1.Our Vision.. (This clicks through to vision page)
Nestled in the North East corner of Tesla Lake , Sk amidst thousands of acres of natural beauty, a unique community is taking shape. A community that connectS people, nature and play. A place to find those simpler times.

2.Explore..(This clicks through to explore page)
Discover a new life of adventure, on the lake fishing, in the bush on our trail system or maybe the local golf course.

3. Live Here..(This through to Live page)
Birch Hollow has everything you need to start living a full life based in a thriving community.
Slow down and get to know nature and your neighbors

Target Market(s)

35-65 Lake Life

Coding

Coded - Design and coding required

Number of Pages Required

5+ page

Font styles to use
Other font styles liked:
• Anntonio

Colors
00AB8E
00BBA5
67D7C9
C6EFE9
E9F9F6
F0912C
F2A743
F7CA91
FBE8D2
FDF5EE

Requirements
Nice to have
• Interactive

```html
<!DOCTYPE html>
<html lang="en">
<head>
<meta charset="utf-8">
<title>Birch Hollow Lodge &amp; Harbour</title>
<link href="https://fonts.googleapis.com/css2?family=Antonio:wght@500;600;700&family=Montserrat:ital,wght@0,400;0,500;0,600;1,400&display=swap" rel="stylesheet">
<style>
:root{
  --teal:#00AB8E;
  --teal-2:#00BBA5;
  --teal-3:#67D7C9;
  --teal-4:#C6EFE9;
  --teal-5:#E9F9F6;
  --orange:#F0912C;
  --orange-2:#F2A743;
  --deep:#0B5E4C;
  --ink:#222;
  --muted:#444;
}
*{box-sizing:border-box;margin:0;padding:0}
html,body{width:1200px;height:3661px;overflow:hidden}
body{position:relative;background:#fff;font-family:"Montserrat",sans-serif;color:var(--ink)}
.abs{position:absolute}
.heading{font-family:"Antonio",sans-serif;font-weight:600;text-transform:uppercase;letter-spacing:.5px}
.btn{position:absolute;display:flex;align-items:center;justify-content:center;font-size:11px;font-weight:600;letter-spacing:.6px;color:#fff;text-transform:uppercase;border-radius:2px;white-space:nowrap}
.btn-teal{background:var(--teal)}
.btn-orange{background:var(--orange)}

/* hero */
.hero{position:absolute;left:0;top:0;width:1200px;height:583px;
  background:linear-gradient(180deg,#2f5fa2 0%,#5f86b8 20%,#c7b79a 36%,#3c5b2d 42%,#2f4a25 52%,#8a6a45 62%,#b58a5b 75%,#6f5a3f 100%)}
.nav-pill{position:absolute;left:156px;top:26px;width:286px;height:31px;background:rgba(255,255,255,.28);border-radius:2px;display:flex;align-items:center}
.nav-pill a{color:#fff;font-size:10px;text-decoration:none;padding:0 10px;height:31px;display:flex;align-items:center;text-transform:uppercase;letter-spacing:.2px;white-space:nowrap}
.nav-pill a.active{background:var(--orange);border-radius:2px}
.brand{position:absolute;left:500px;top:14px;width:200px;text-align:center;color:#fff}
.brand .mark{width:12px;height:12px;background:#fff;margin:0 auto 8px}
.brand .name{font-family:"Antonio",sans-serif;font-weight:600;font-size:20px;line-height:1.15;letter-spacing:1px;text-transform:uppercase;white-space:nowrap}
.contact-btn{left:941px;top:26px;width:108px;height:31px}
.booking{position:absolute;left:385px;top:290px;width:425px;height:38px;background:rgba(255,255,255,.3);display:flex;align-items:center;color:#fff;font-size:10px;white-space:nowrap}
.booking .field{display:flex;align-items:center;gap:6px;padding:0 16px;height:100%;border-right:1px solid rgba(255,255,255,.45)}
.booking .book{margin-left:auto;height:32px;margin-right:4px;position:static;padding:0 18px}
.divider{position:absolute;left:0;width:1200px;height:40px}
.mouse{position:absolute;left:591px;top:576px}

/* features */
.feature{position:absolute;width:230px;text-align:center}
.feature .icon{width:76px;height:97px;margin:0 auto;display:block}
.feature h2{font-size:33px;color:#333;margin-top:18px;font-weight:600}
.feature p{font-size:10px;line-height:15px;color:var(--muted);margin-top:10px}

/* tinted sections */
.tint{position:absolute;left:0;width:1200px;background:linear-gradient(135deg,#e4f1ee 0%,#d3e3e0 50%,#c9dbd8 100%)}
.title-teal{color:var(--teal);font-size:40px}
.amenity{position:absolute;width:120px}
.amenity svg{display:block}
.amenity span{display:block;font-size:11px;color:#333;margin-top:2px;line-height:13px}
.photo{position:absolute}

/* testimonial */
.quote-text{position:absolute;left:280px;top:1925px;width:640px;text-align:center;font-style:italic;font-size:12.5px;line-height:23px;color:#333}

/* newsletter */
.stay h2{font-size:40px;color:#111}
.input{position:absolute;left:493px;top:3199px;width:272px;height:31px;border:1px solid #d6d6d6;background:#fff;font-size:10px;color:#999;padding:0 18px;display:flex;align-items:center}

/* footer */
.footer{position:absolute;left:0;top:3345px;width:1200px;height:316px;background:var(--deep)}
.footer-title{position:absolute;top:3403px;font-family:"Antonio",sans-serif;font-weight:600;font-size:19px;color:#fff;letter-spacing:.5px;text-transform:uppercase}
.contact-line{position:absolute;display:flex;align-items:flex-start;gap:10px;color:#fff;font-size:11.5px;line-height:17px;white-space:nowrap}
.contact-line svg{flex:none;margin-top:2px}
.links{position:absolute;left:601px;top:3441px;list-style:none;color:#fff;font-size:11.5px;line-height:19.4px}
.links li.current{color:var(--orange);text-decoration:underline}
.footer-brand{position:absolute;left:120px;top:3450px;width:155px;text-align:center;color:#fff}
.footer-brand .mark{width:14px;height:14px;background:#fff;margin:0 auto 12px}
.footer-brand .name{font-family:"Antonio",sans-serif;font-weight:600;font-size:19px;line-height:1.25;letter-spacing:1px;text-transform:uppercase;white-space:nowrap}
.bottom-bar{position:absolute;left:0;top:3633px;width:1200px;height:28px;background:var(--teal);color:#fff;font-size:10px;display:flex;align-items:center;padding-left:149px}
.social{position:absolute;top:3639px;width:16px;height:16px;border-radius:50%;background:rgba(255,255,255,.3)}
</style>
</head>
<body>

<!-- HERO -->
<section class="hero" role="img" aria-label="Lakeside dock with boats and cottages at sunset under a blue sky"></section>
<nav class="nav-pill">
  <a class="active" href="#">Home</a><a href="#">Our Vision</a><a href="#">Explore</a><a href="#">Live Here</a>
</nav>
<div class="brand">
  <div class="mark"></div>
  <div class="name">Birch Hollow<br>Lodge &amp; Harbour</div>
</div>
<a class="btn btn-teal contact-btn">Contact Us</a>
<div class="booking">
  <div class="field"><svg width="11" height="11" viewBox="0 0 11 11" fill="none" stroke="#fff"><rect x=".5" y="1.5" width="10" height="9"/><line x1=".5" y1="4" x2="10.5" y2="4"/></svg>Check In</div>
  <div class="field"><svg width="11" height="11" viewBox="0 0 11 11" fill="none" stroke="#fff"><rect x=".5" y="1.5" width="10" height="9"/><line x1=".5" y1="4" x2="10.5" y2="4"/></svg>Check Out</div>
  <div class="field" style="border:none"><svg width="11" height="11" viewBox="0 0 11 11" fill="none" stroke="#fff"><circle cx="5.5" cy="3.5" r="2.5"/><path d="M1 10.5c0-3 9-3 9 0"/></svg>Guest</div>
  <a class="btn btn-orange book">Book Now</a>
</div>
<svg class="divider" style="top:543px" viewBox="0 0 1200 40" preserveAspectRatio="none">
  <polygon points="400,40 600,2 800,40" fill="#fff"/>
  <polyline points="400,40 600,2 800,40" fill="none" stroke="#00AB8E" stroke-width="4"/>
</svg>
<svg class="mouse" width="18" height="34" viewBox="0 0 18 34" fill="none" stroke="#777" stroke-width="1.2">
  <rect x="2" y="1" width="14" height="20" rx="7"/><line x1="9" y1="5" x2="9" y2="9"/><path d="M9 24v8M6 29l3 3 3-3"/>
</svg>

<!-- FEATURES -->
<div class="feature" style="left:211px;top:665px">
  <svg class="icon" viewBox="0 0 76 97" fill="none"><path d="M2 22 38 2l36 20v73H2z" stroke="#cfe3df" stroke-width="2"/>
    <g stroke="#00AB8E" stroke-width="3" fill="#00AB8E"><path d="M20 52l30-14 4 8-30 14z"/><line x1="36" y1="54" x2="28" y2="74"/><line x1="36" y1="54" x2="44" y2="74"/><line x1="36" y1="54" x2="36" y2="74"/></g></svg>
  <h2 class="heading">Our Vision</h2>
  <p>Nestled in the North East corner of Loonwater Lake, amidst thousands of acres of natural beauty, a unique community is taking shape. A community that connectS people, nature and play. A place to find those simpler times.</p>
</div>
<div class="feature" style="left:485px;top:665px">
  <svg class="icon" viewBox="0 0 76 97" fill="none"><path d="M2 22 38 2l36 20v73H2z" stroke="#cfe3df" stroke-width="2"/>
    <circle cx="38" cy="54" r="18" stroke="#00AB8E" stroke-width="3"/><path d="M38 38l4 12 12 4-12 4-4 12-4-12-12-4 12-4z" fill="#00AB8E"/></svg>
  <h2 class="heading">Explore</h2>
  <p>Discover&nbsp; a new life of adventure, on the lake fishing, in the bush on our trail system or maybe the local golf course.</p>
</div>
<div class="feature" style="left:757px;top:665px">
  <svg class="icon" viewBox="0 0 76 97" fill="none"><path d="M2 22 38 2l36 20v73H2z" stroke="#cfe3df" stroke-width="2"/>
    <g stroke="#00AB8E" stroke-width="3"><circle cx="38" cy="54" r="3" fill="#00AB8E"/><path d="M31 47a10 10 0 0 0 0 14M45 47a10 10 0 0 1 0 14M25 41a18 18 0 0 0 0 26M51 41a18 18 0 0 1 0 26"/></g></svg>
  <h2 class="heading">Live Here</h2>
  <p>Birch Hollow has everything you need to start living a full life based in a thriving community.</p>
</div>
<a class="btn btn-teal" style="left:549px;top:943px;width:96px;height:31px">Book Now</a>

<!-- AMENITIES -->
<svg class="divider" style="top:1050px" viewBox="0 0 1200 40" preserveAspectRatio="none">
  <polygon points="400,40 600,2 800,40" fill="#e0eeeb"/>
  <polyline points="400,40 600,2 800,40" fill="none" stroke="#00AB8E" stroke-width="4"/>
</svg>
<section class="tint" style="top:1089px;height:603px"></section>
<h2 class="heading title-teal abs" style="left:200px;top:1174px">Amenities</h2>

<div class="amenity" style="left:200px;top:1248px">
  <svg width="58" height="68" viewBox="0 0 58 68" fill="none"><path d="M2 16 29 2l27 14v50H2z" stroke="#c9ddd9" stroke-width="1.5"/><g stroke="#00AB8E" stroke-width="2"><rect x="12" y="26" width="32" height="7" rx="3"/><rect x="12" y="35" width="32" height="7" rx="3"/><rect x="12" y="44" width="32" height="7" rx="3"/></g></svg>
  <span>Few Casual<br>Clothes</span>
</div>
<div class="amenity" style="left:340px;top:1248px">
  <svg width="58" height="68" viewBox="0 0 58 68" fill="none"><path d="M2 16 29 2l27 14v50H2z" stroke="#c9ddd9" stroke-width="1.5"/><g stroke="#00AB8E" stroke-width="2"><path d="M14 38h30a15 12 0 0 1-30 0z"/><circle cx="24" cy="31" r="4"/><circle cx="33" cy="29" r="4"/></g></svg>
  <span>Little Food</span>
</div>
<div class="amenity" style="left:479px;top:1248px">
  <svg width="58" height="68" viewBox="0 0 58 68" fill="none"><path d="M2 16 29 2l27 14v50H2z" stroke="#c9ddd9" stroke-width="1.5"/><g stroke="#00AB8E" stroke-width="2"><rect x="12" y="36" width="34" height="10"/><path d="M14 36V26h30v10M12 46v5M46 46v5"/><rect x="18" y="30" width="8" height="5"/><rect x="32" y="30" width="8" height="5"/></g></svg>
  <span>Queen/King<br>Luxurious bed</span>
</div>
<div class="amenity" style="left:200px;top:1368px">
  <svg width="58" height="68" viewBox="0 0 58 68" fill="none"><path d="M2 16 29 2l27 14v50H2z" stroke="#c9ddd9" stroke-width="1.5"/><g stroke="#00AB8E" stroke-width="2"><path d="M12 36h34v6a8 8 0 0 1-8 8H20a8 8 0 0 1-8-8z"/><path d="M16 36V24a4 4 0 0 1 8 0"/><line x1="20" y1="50" x2="18" y2="55"/><line x1="38" y1="50" x2="40" y2="55"/></g></svg>
  <span>Private Bathroom</span>
</div>
<div class="amenity" style="left:340px;top:1368px">
  <svg width="58" height="68" viewBox="0 0 58 68" fill="none"><path d="M2 16 29 2l27 14v50H2z" stroke="#c9ddd9" stroke-width="1.5"/><g stroke="#00AB8E" stroke-width="2"><rect x="30" y="22" width="12" height="16"/><path d="M14 36h26a10 10 0 0 1-10 10h-6a10 10 0 0 1-10-10z"/><path d="M22 46v8h10v-8"/></g></svg>
  <span>Flushing Toilet</span>
</div>
<div class="amenity" style="left:479px;top:1368px">
  <svg width="58" height="68" viewBox="0 0 58 68" fill="none"><path d="M2 16 29 2l27 14v50H2z" stroke="#c9ddd9" stroke-width="1.5"/><g stroke="#00AB8E" stroke-width="2"><path d="M18 22v10a3 3 0 0 0 6 0V22M21 32v24M36 22c-4 0-4 14 0 14v20M34 22v34"/></g></svg>
  <span>Kitchen Area</span>
</div>
<div class="abs" style="left:200px;top:1488px;width:349px;height:4px;background:#fff;border-radius:2px"></div>
<div class="abs" style="left:205px;top:1488px;width:57px;height:4px;background:var(--orange);border-radius:2px"></div>
<a class="btn btn-orange" style="left:200px;top:1524px;width:97px;height:31px">Book Now</a>

<svg class="abs" style="left:644px;top:1160px" width="240" height="405" viewBox="0 0 240 405" fill="none" stroke="#00AB8E" stroke-width="1.5">
  <polyline points="182,1 1,57 1,403 232,403"/>
</svg>
<div class="photo" role="img" aria-label="Woman relaxing with a dog in front of a glamping tent" style="left:655px;top:1174px;width:345px;height:379px;clip-path:polygon(0 9%,50% 0,100% 9%,100% 100%,0 100%);background:linear-gradient(160deg,#d8b27e 0%,#b98d55 40%,#4e5d2e 75%,#7a2a22 100%)"></div>

<svg class="divider" style="top:1652px" viewBox="0 0 1200 40" preserveAspectRatio="none">
  <polygon points="400,40 600,2 800,40" fill="#fff"/>
  <polyline points="400,40 600,2 800,40" fill="none" stroke="#00AB8E" stroke-width="4"/>
</svg>

<!-- TESTIMONIALS -->
<h2 class="heading title-teal abs" style="left:0;width:1200px;text-align:center;top:1762px">Happy Clients Say</h2>
<div class="abs" style="left:567px;top:1835px;width:66px;height:66px;border-radius:50%;background:var(--teal);display:flex;align-items:center;justify-content:center;color:#fff;font-family:'Antonio',sans-serif;font-size:34px;font-weight:700">66</div>
<svg class="abs" style="left:199px;top:1937px" width="12" height="18" viewBox="0 0 12 18" fill="none" stroke="#00AB8E" stroke-width="2.5"><path d="M10 2 3 9l7 7"/></svg>
<svg class="abs" style="left:989px;top:1937px" width="12" height="18" viewBox="0 0 12 18" fill="none" stroke="#00AB8E" stroke-width="2.5"><path d="M2 2l7 7-7 7"/></svg>
<p class="quote-text">“ Lorem Ipsum is simply dummy text of the printing and typesetting industry. Lorem Ipsum has been the industry's standard dummy text ever since the 1500s, when an unknown printer took a galley of type and scrambled it to make a type specimen book. ”</p>
<p class="abs" style="left:0;width:1200px;text-align:center;top:2012px;font-size:11px;font-weight:600">Standard Chunk</p>
<a class="btn btn-teal" style="left:549px;top:2059px;width:104px;height:31px">View All</a>

<!-- GALLERY -->
<svg class="divider" style="top:2166px" viewBox="0 0 1200 40" preserveAspectRatio="none">
  <polygon points="400,40 600,2 800,40" fill="#e0eeeb"/>
  <polyline points="400,40 600,2 800,40" fill="none" stroke="#00AB8E" stroke-width="4"/>
</svg>
<section class="tint" style="top:2205px;height:806px"></section>
<h2 class="heading title-teal abs" style="left:0;width:1200px;text-align:center;top:2260px">Gallery</h2>
<div class="photo" role="img" aria-label="Family playing together in front of a canvas bell tent" style="left:200px;top:2332px;width:288px;height:500px;background:linear-gradient(170deg,#d9d3c2 0%,#cdbd9f 40%,#6b8a4a 75%,#4e6c35 100%)"></div>
<div class="photo" role="img" aria-label="Woman in a sun hat holding a drink by the pool" style="left:500px;top:2332px;width:244px;height:244px;background:linear-gradient(160deg,#9fc9e4 0%,#3f72b0 40%,#6aa3c4 70%,#c9a98a 100%)"></div>
<div class="photo" role="img" aria-label="Raised safari tent among green trees" style="left:756px;top:2332px;width:244px;height:244px;background:linear-gradient(170deg,#e8eef0 0%,#7fa05a 45%,#3f5f2a 100%)"></div>
<div class="photo" role="img" aria-label="Evening table set with food and candles beside a tent" style="left:500px;top:2589px;width:500px;height:243px;background:linear-gradient(170deg,#3a4030 0%,#8a6a3b 35%,#c58a3a 60%,#4a2f1d 100%)"></div>
<a class="btn btn-orange" style="left:549px;top:2865px;width:104px;height:31px">View All</a>
<svg class="divider" style="top:2971px" viewBox="0 0 1200 40" preserveAspectRatio="none">
  <polygon points="400,40 600,2 800,40" fill="#fff"/>
  <polyline points="400,40 600,2 800,40" fill="none" stroke="#00AB8E" stroke-width="4"/>
</svg>

<!-- NEWSLETTER -->
<svg class="abs" style="left:307px;top:3078px" width="141" height="161" viewBox="0 0 141 161" fill="none">
  <path d="M2 28 70.5 2 139 28v131H2z" stroke="#d9e6e3" stroke-width="2"/>
  <g stroke="#00AB8E" stroke-width="5" stroke-linejoin="round">
    <path d="M30 82v50h81V82"/><path d="M30 82l40 30 41-30"/><path d="M30 132l30-24M111 132l-30-24"/>
    <rect x="46" y="46" width="49" height="52" fill="#fff"/>
    <line x1="56" y1="60" x2="85" y2="60"/><line x1="56" y1="71" x2="85" y2="71"/><line x1="56" y1="82" x2="78" y2="82"/>
  </g>
</svg>
<div class="stay">
  <h2 class="heading abs" style="left:493px;top:3098px">Stay In Touch</h2>
  <p class="abs" style="left:493px;top:3153px;font-size:12px;line-height:16px;color:var(--teal);font-weight:500;width:330px">Sign up to be the first to know about our deals and special offers.</p>
</div>
<div class="input">Your email address*</div>
<a class="btn btn-teal" style="left:771px;top:3199px;width:122px;height:31px">Subscribe Now</a>

<!-- FOOTER -->
<svg class="divider" style="top:3306px" viewBox="0 0 1200 40" preserveAspectRatio="none">
  <polygon points="400,40 600,2 800,40" fill="#0B5E4C"/>
  <polyline points="400,40 600,2 800,40" fill="none" stroke="#00AB8E" stroke-width="4"/>
</svg>
<footer class="footer"></footer>
<div class="footer-brand">
  <div class="mark"></div>
  <div class="name">Birch Hollow<br>Lodge &amp; Harbour</div>
</div>

<h3 class="footer-title" style="left:340px">Conatct Info</h3>
<div class="contact-line" style="left:340px;top:3440px"><svg width="12" height="15" viewBox="0 0 12 15"><path d="M6 0a6 6 0 0 1 6 6c0 4-6 9-6 9S0 10 0 6a6 6 0 0 1 6-6z" fill="#67D7C9"/><circle cx="6" cy="6" r="2" fill="#0B5E4C"/></svg><span>412 Lorem ipsum Maple<br>Rd., Fernvale, CA95011</span></div>
<div class="contact-line" style="left:340px;top:3487px"><svg width="12" height="12" viewBox="0 0 12 12"><path d="M2 0h3l1 3-2 1a7 7 0 0 0 4 4l1-2 3 1v3a2 2 0 0 1-2 2A10 10 0 0 1 0 2a2 2 0 0 1 2-2z" fill="#67D7C9"/></svg><span>(555) 204-7188</span></div>
<div class="contact-line" style="left:340px;top:3518px"><svg width="13" height="10" viewBox="0 0 13 10"><rect width="13" height="10" fill="#67D7C9"/><path d="M0 0l6.5 5L13 0" stroke="#0B5E4C" fill="none"/></svg><span>hello@birchhollowlodge.com</span></div>
<div class="contact-line" style="left:340px;top:3550px"><svg width="13" height="13" viewBox="0 0 13 13" fill="none" stroke="#67D7C9" stroke-width="1.5"><circle cx="6.5" cy="6.5" r="5.5"/><path d="M1 6.5h11M6.5 1c3 3 3 8 0 11M6.5 1c-3 3-3 8 0 11"/></svg><span>live location</span></div>

<h3 class="footer-title" style="left:601px">Quick Link</h3>
<ul class="links">
  <li class="current">Home</li><li>Our Vision</li><li>Explore</li><li>Live Here</li><li>Contact Us</li><li>Privacy Policy</li><li>Terms &amp; Conditions</li>
</ul>
<div class="abs" role="img" aria-label="Map showing the lodge location on the west coast" style="left:788px;top:3408px;width:261px;height:158px;background:linear-gradient(90deg,#a9d3e8 0%,#a9d3e8 22%,#e9ecd8 30%,#f1efe4 100%)"></div>

<div class="bottom-bar">© 2023 Birch Hollow Lodge &amp; Harbour. All Right Reserved</div>
<span class="social" style="left:955px"></span>
<span class="social" style="left:980px"></span>
<span class="social" style="left:1005px;background:var(--orange)"></span>
<span class="social" style="left:1031px"></span>

</body>
</html>
```